Unique & Creative Business Card for Lumavessence

Would you please create a unique design that is soft and appealing to people who seek to raise vibrational energy for themselves, for animals (domestic or wild), or for the environment.

Optional: Elements could include, landscapes, wild animals, feathers, vibrational patterns, the elements (Earth, water, fire, air and space). Images that are calming.

With Thanks!

Target Market(s)

People and businesses who are into the environment, animal welfare, alternative health.

Contact Information for Business Card

Moira Bell
Energist
mb@lumavessence.example
lumavessence.example

Requirements
Must have
• Lumavessence logo (attached)
Symbols that represent our main services: Earth, wild creatures, people and inner light.
Our promise ‘Restoring Gentle Resonant Harmony’
Nice to have
• Clear and easy to read
Colours based on nature/soft colours

```html
<!DOCTYPE html>
<html lang="en">
<head>
<meta charset="utf-8">
<title>Lumavessence Business Card</title>
<link href="https://fonts.googleapis.com/css2?family=Work+Sans:wght@400;500;700&display=swap" rel="stylesheet">
<style>
  :root {
    --page-bg: #2b2b2b;
    --card-white: #ffffff;
    --brand-blue: #2d4a93;
    --text-grey: #5a5a62;
    --rule-grey: #9aa3bd;
    --sky-top: #6d6c6e;
    --sky-mid: #7d7676;
    --forest: #2f5a60;
    --forest-deep: #1e3c42;
    --lilac: #e6e0ee;
  }
  * { margin: 0; padding: 0; box-sizing: border-box; }
  html, body { width: 1200px; height: 930px; overflow: hidden; }
  body {
    background: var(--page-bg);
    font-family: "Work Sans", sans-serif;
    position: relative;
  }
  .card {
    position: absolute;
    width: 700px;
    height: 400px;
    border-radius: 22px;
    overflow: hidden;
  }
  .card-front { left: 130px; top: 45px; }
  .card-back { left: 370px; top: 485px; background: var(--card-white); }

  .landscape-photo {
    position: absolute; inset: 0;
    background: linear-gradient(180deg, var(--sky-top) 0%, var(--sky-mid) 30%, var(--forest) 62%, var(--forest-deep) 100%);
  }
  .front-brand {
    position: absolute;
    left: 50%; top: 145px;
    transform: translateX(-50%);
    display: flex; align-items: center; gap: 14px;
    white-space: nowrap;
  }
  .brand-dot {
    width: 26px; height: 26px;
    border-radius: 50%;
    border: 3px solid var(--lilac);
    flex: none;
  }
  .front-brand .brand-name {
    font-size: 36px; font-weight: 500; letter-spacing: 1px;
    color: var(--card-white); text-transform: uppercase;
  }
  .front-services {
    position: absolute;
    left: 40px; bottom: 38px;
    color: var(--card-white);
    font-size: 19px; line-height: 1.4;
  }

  .back-brand {
    position: absolute;
    left: 40px; top: 180px;
    display: flex; align-items: center; gap: 12px;
    white-space: nowrap;
  }
  .back-brand .brand-dot { border-color: var(--brand-blue); width: 22px; height: 22px; }
  .back-brand .brand-name {
    font-size: 28px; font-weight: 500; letter-spacing: 1px;
    color: var(--brand-blue); text-transform: uppercase;
  }
  .divider {
    position: absolute;
    left: 355px; top: 90px;
    width: 1px; height: 220px;
    background: var(--rule-grey);
  }
  .contact-block {
    position: absolute;
    left: 400px; top: 110px;
  }
  .person-name {
    font-size: 34px; font-weight: 700; letter-spacing: 2px;
    color: var(--brand-blue); text-transform: uppercase; line-height: 1;
  }
  .person-role {
    font-size: 18px; color: var(--text-grey); margin: 6px 0 16px 4px;
  }
  .contact-list { list-style: none; }
  .contact-list li {
    display: flex; align-items: center; gap: 8px;
    font-size: 17px; color: var(--text-grey); margin-bottom: 6px;
    white-space: nowrap;
  }
  .contact-list svg { width: 14px; height: 14px; flex: none; }
</style>
</head>
<body>

<section class="card card-front">
  <div class="landscape-photo" role="img" aria-label="Misty mountain valley with pine forest and river at dusk"></div>
  <div class="front-brand">
    <span class="brand-dot"></span>
    <span class="brand-name">Lumavessence</span>
  </div>
  <p class="front-services">
    Earth, wild creatures, people and inner light.<br>
    Our promise ‘Restoring Gentle Resonant Harmony’
  </p>
</section>

<section class="card card-back">
  <div class="back-brand">
    <span class="brand-dot"></span>
    <span class="brand-name">Lumavessence</span>
  </div>
  <div class="divider"></div>
  <div class="contact-block">
    <h1 class="person-name">Moira Bell</h1>
    <p class="person-role">Energist</p>
    <ul class="contact-list">
      <li>
        <svg viewBox="0 0 16 16" fill="var(--brand-blue)"><path d="M3.6 1.5l2.3 2.6-1.4 1.8c.9 2 2.4 3.6 4.5 4.6l1.8-1.4 2.6 2.3-1.6 2.1C6.5 13.3 2.6 9.4 1.5 3.1z"/></svg>
        06.12.34.57.80
      </li>
      <li>
        <svg viewBox="0 0 16 16" fill="none" stroke="var(--brand-blue)" stroke-width="1.6"><rect x="1.5" y="3.5" width="13" height="9" rx="1"/><path d="M1.5 4l6.5 5 6.5-5"/></svg>
        mb@lumavessence.example
      </li>
      <li>
        <svg viewBox="0 0 16 16" fill="none" stroke="var(--brand-blue)" stroke-width="1.4"><circle cx="8" cy="8" r="6.5"/><ellipse cx="8" cy="8" rx="3" ry="6.5"/><path d="M1.5 8h13M2.5 5h11M2.5 11h11"/></svg>
        www.lumavessence.example
      </li>
    </ul>
  </div>
</section>

</body>
</html>
```